Flyer-Design für Gefäßchirurg
Zielgruppe
Niedergelassener Gefäßchirurg in eigener (Einzel-) Praxis; zZt 4 Angestellte (1 Krankenschwester, eine MFA, eine Azubi, eine Reinigungskraft); tätig in der Stadt Plön (24306); im Kreis Plön nur ein weiter ALLGEMEIN chirurg; HP: www.praxisdoktor-haverbeck.de ; Kernkompetenz: Diagnostik und Therapie von Gefäßerkrankungen (z.B. Krampfadern, Durchblutungsstörungen... (s.auch HP); eigener OP in der Praxis; hier Versorgung u.a. von Krampfadern aber auch andere chirurgische Eingriffe;
Aufgabenstellung
Bzgl. des Formates keine Festlegung bevorzuge aber Format Din lang hoch oder Din a 5 hoch ; Flyer soll übersichtlich Behandlungen der Praxis benennen; insbesondere um auch außerhalb der Gefäßchirurgie weitere chirurgische Patienten zu gewinnen (z.B. chirurgische Entfernung kleiner Pigmentflecke, eingewachsener Nagel, aber auch 'Wegspritzen/ Sklerosierung' von Besenreisern, eingewachsener Zehennagel), ggf. mit Anfahrtskarte, Parkplätze vor der Tür; falls nicht zu Kostenintensiv: auch Nutzung von Stock - Bildern (ca. Obergrenze für Bildmaterial 50,- €);
mir ist bewusst, dass die Photos der Angestellten und mir nicht 100% scharf sind; falls diese verwendet werden, könnten diese z.B. kleinformatig auf dem flyer erscheinen, oder ich würde diese im Verlauf noch einmal aufnehmen. Ob und wieviele der Photos auf dem flyer sind, überlasse ich Ihnen.

```html
<!DOCTYPE html>
<html lang="de">
<head>
<meta charset="utf-8">
<title>Flyer Praxis für Gefäßmedizin und Chirurgie</title>
<link href="https://fonts.googleapis.com/css2?family=Montserrat:ital,wght@0,400;0,500;0,600;0,700;0,800;1,400&display=swap" rel="stylesheet">
<style>
  :root{
    --red:#d1232d;
    --red-dark:#b51d26;
    --slate:#4a4a4c;
    --paper:#ffffff;
    --paper-grey:#eeeeef;
    --ink:#555558;
    --ink-soft:#77777a;
    --stage:#e9e9ea;
  }
  *{box-sizing:border-box;margin:0;padding:0}
  html,body{width:1200px;height:2373px;overflow:hidden}
  body{background:var(--stage);font-family:"Montserrat",sans-serif;color:var(--ink);
    display:flex;flex-direction:column;align-items:center;justify-content:center;gap:110px}
  .spread{width:1100px;height:777px;display:flex;background:var(--paper);
    border-top:4px solid var(--red);border-bottom:4px solid var(--red);
    box-shadow:0 12px 30px rgba(0,0,0,.12)}
  .panel{width:33.333%;height:100%;position:relative;padding:34px 30px;overflow:hidden}
  .panel + .panel{border-left:1px solid #e2e2e2}
  .panel--light{background:linear-gradient(180deg,#f4f4f5,#e7e7e8)}
  .panel--dark{background:var(--slate);color:#fff}
  .photo{border-radius:50%;background:radial-gradient(circle at 45% 40%,#dfe3e8,#b9bec6)}
  p{font-size:10px;line-height:1.5;margin-bottom:7px}

  .brand{text-align:right}
  .brand__name{font-weight:700;font-size:20px;letter-spacing:.3px;color:var(--slate);display:flex;align-items:center;justify-content:flex-end;gap:8px}
  .brand__dot{width:14px;height:14px;border-radius:50%;background:var(--red)}
  .brand__sub{font-size:9px;color:var(--ink-soft);margin-top:3px}
  .panel--dark .brand__name,.panel--dark .brand__sub{color:#fff}

  .kicker{font-size:12px;font-weight:600;color:var(--ink)}
  .heading{font-size:26px;font-weight:700;color:var(--red);line-height:1.05;margin-bottom:12px}
  .kicker::after{content:"";display:inline-block;width:70px;height:1.5px;background:var(--red);margin-left:8px;vertical-align:middle}

  .doctor-photo{position:absolute;top:18px;right:36px;width:128px;height:128px;background:radial-gradient(circle at 50% 40%,#e7c9a7,#b9b3aa)}
  .praxis{margin-top:150px}
  .team{display:flex;justify-content:space-between;margin-top:14px}
  .member{width:96px;text-align:center}
  .member .photo{width:80px;height:80px;margin:0 auto 8px;background:radial-gradient(circle at 50% 40%,#e3c2a4,#a39384)}
  .member__name{font-size:10px;color:var(--ink)}
  .member__role{display:block;background:var(--red);color:#fff;font-size:9px;font-weight:600;padding:2px 0;margin-top:3px}

  .map{width:240px;height:240px;margin:26px auto 0;background:radial-gradient(circle,#f7f7f7,#d8dde2)}
  .badge{position:absolute;border-radius:50%;background:var(--red);color:#fff;text-align:center;display:flex;flex-direction:column;align-items:center;justify-content:center;font-weight:800;line-height:1.05}
  .badge--street{width:88px;height:88px;top:230px;right:44px;font-size:11px;transform:rotate(-10deg)}
  .badge--street small{font-size:7.5px;font-weight:600}
  .contact{list-style:none;margin-top:30px}
  .contact li{display:flex;align-items:center;gap:10px;font-size:10.5px;margin-bottom:11px}
  .contact svg{flex:none}
  .hours{font-size:10.5px;line-height:1.45;margin-left:28px}
  .hours strong{display:block;font-weight:700;margin:6px 0 4px}
  .url{position:absolute;left:30px;right:30px;bottom:44px;padding-top:12px;border-top:1.5px solid var(--red);font-weight:700;font-size:13.5px;text-align:center}

  .cover-photo{position:absolute;top:110px;left:30px;width:330px;height:330px;background:radial-gradient(circle at 55% 60%,#c9cfd8,#eef0f3 70%)}
  .badge--cta{width:124px;height:124px;top:390px;left:40px;font-size:20px;transform:rotate(-10deg)}
  .badge--cta em{font-style:normal;font-weight:500;font-size:13px}
  .cover-title{position:absolute;left:30px;right:24px;top:560px;color:var(--red);font-weight:700;font-size:34px;line-height:1.15}
  .cover-title .und{font-size:16px;color:var(--ink);font-weight:600;text-decoration:underline;text-underline-offset:3px;margin-right:6px}

  .service{margin-bottom:12px}
  .service__title{font-size:13px;font-weight:500;color:var(--red);border-bottom:1px solid var(--red);padding-bottom:3px;margin-bottom:6px;display:flex;align-items:center;gap:8px}
  .service__title::before{content:"";width:16px;height:16px;border:1.5px solid var(--ink-soft);border-radius:50%;flex:none}
  .cells-photo{width:230px;height:230px;margin:0 auto 18px;display:block;background:radial-gradient(circle at 40% 45%,#e0303a,#7e0c12 75%)}
  .badge--cells{width:92px;height:92px;top:110px;left:26px;font-size:13px}
  .badge--cells em{font-style:normal;font-weight:500;font-size:9px}
  .appointment{background:var(--slate);color:#fff;margin:-34px -30px 20px;padding:26px 26px 20px;text-align:center}
  .appointment p{font-size:10px;font-weight:600}
  .hotline{display:flex;align-items:center;gap:12px;border:1.5px solid var(--red);padding:8px 12px;text-align:left;margin-top:8px}
  .hotline__num{font-size:22px;font-weight:800;display:block;line-height:1.1}
  .hotline small{font-size:9.5px}
</style>
</head>
<body>

<section class="spread spread--outside">
  <article class="panel panel--light">
    <div class="photo doctor-photo" role="img" aria-label="Porträt des Praxisinhabers"></div>
    <div class="praxis">
      <div class="kicker">Die</div>
      <h2 class="heading">Praxis</h2>
      <p>Gerne kümmern wir uns um Ihre chirurgischen und gefäßmedizinischen Anliegen.</p>
      <p>Als Gefäßchirurg und Phlebologe besitze ich eine besondere Erfahrung in der Therapie und Diagnostik von gefäßmedizinischen Erkrankungen. Mit einem hochwertigen Ultraschallgerät sowie einem eigenen Operationsraum und einem Aufwachraum sind optimale Bedingungen gegeben.</p>
      <p>Bezüglich der operativen Versorgung des Krampfaderleidens halten wir alle gängigen Operationsmethoden vor.</p>
      <p>Abseits der gefäßmedizinischen Erkrankungen sind wir auch für kleinere chirurgische Maßnahmen Ihr Ansprechpartner.</p>
    </div>
    <div style="margin-top:22px">
      <div class="kicker">Das</div>
      <h2 class="heading">Praxisteam</h2>
      <p>Unterstützt wird mein Team durch eine Krankenschwester, eine Medizinische Fachangestellte und eine Auszubildende.</p>
      <div class="team">
        <figure class="member"><div class="photo" role="img" aria-label="Porträt Krankenschwester"></div><figcaption class="member__name">Jana Kröger<span class="member__role">Krankenschwester</span></figcaption></figure>
        <figure class="member"><div class="photo" role="img" aria-label="Porträt Medizinische Fachangestellte"></div><figcaption class="member__name">Sabine Lorenz<span class="member__role">MFA</span></figcaption></figure>
        <figure class="member"><div class="photo" role="img" aria-label="Porträt Auszubildende"></div><figcaption class="member__name">Elif Demir<span class="member__role">Auszubildende</span></figcaption></figure>
      </div>
    </div>
  </article>

  <article class="panel panel--dark">
    <div class="brand">
      <div class="brand__name">Dr. Rolf Haverbeck <span class="brand__dot"></span></div>
      <div class="brand__sub">Praxis für Gefäßmedizin und Chirurgie</div>
    </div>
    <div class="photo map" role="img" aria-label="Anfahrtskarte zur Praxis in Lindenau"></div>
    <div class="badge badge--street">LINDENWEG<small>IN LINDENAU</small></div>
    <ul class="contact">
      <li><svg width="18" height="18" viewBox="0 0 18 18"><circle cx="9" cy="9" r="9" fill="#d1232d"/><path d="M9 4a3 3 0 0 0-3 3c0 2.3 3 6 3 6s3-3.7 3-6a3 3 0 0 0-3-3z" fill="#fff"/></svg>Lindenweg 12 | 23715 Lindenau</li>
      <li><svg width="18" height="18" viewBox="0 0 18 18"><circle cx="9" cy="9" r="9" fill="#d1232d"/><path d="M5 7c0-1 1-2 4-2s4 1 4 2v1h-2V7H7v1H5zM6 9h6l1 4H5z" fill="#fff"/></svg>Telefon: 04531 5813 240</li>
      <li><svg width="18" height="18" viewBox="0 0 18 18"><circle cx="9" cy="9" r="9" fill="#d1232d"/><rect x="5" y="7" width="8" height="6" fill="#fff"/><rect x="6.5" y="4.5" width="5" height="3" fill="#fff"/></svg>Fax: 04531 5813 249</li>
      <li><svg width="18" height="18" viewBox="0 0 18 18"><circle cx="9" cy="9" r="9" fill="#d1232d"/><rect x="4.5" y="6" width="9" height="6.5" fill="#fff"/><path d="M4.5 6l4.5 4 4.5-4" stroke="#d1232d" fill="none"/></svg>info@praxisdoktor-haverbeck.de</li>
    </ul>
    <div class="hours">
      <strong>ÖFFNUNGSZEITEN:</strong>
      Montag, Mittwoch, Donnerstag, Freitag:<br>08:00 – 13:00 Uhr<br><br>
      Dienstag:<br>08:00 – 13:00 13:00 – 15:00 Uhr
    </div>
    <div class="url">www.praxisdoktor-haverbeck.de</div>
  </article>

  <article class="panel">
    <div class="brand">
      <div class="brand__name">Dr. Rolf Haverbeck <span class="brand__dot"></span></div>
      <div class="brand__sub">Praxis für Gefäßmedizin und Chirurgie</div>
    </div>
    <div class="photo cover-photo" role="img" aria-label="Stethoskop auf einem Arzttisch"></div>
    <div class="badge badge--cta">JETZT<br>TERMIN<em>vereinbaren</em></div>
    <h1 class="cover-title">Chirurgie<br><span class="und">und</span>Gefäßmedizin</h1>
  </article>
</section>

<section class="spread spread--inside">
  <article class="panel panel--light">
    <div class="kicker">Unsere</div>
    <h2 class="heading">Leistungen</h2>
    <div class="service">
      <h3 class="service__title">Krampfadern</h3>
      <p>Nach entsprechender Diagnostik stehen Ihnen je nach Befund und Wunsch die konservative Therapie, die operative Entfernung der erkrankten Venenanteile oder die schonende Behandlung mittels Laser in unserer Praxis unter ambulanten Bedingungen zur Verfügung.</p>
    </div>
    <div class="service">
      <h3 class="service__title">Besenreiser</h3>
      <p>Feine, erweiterte Venen an den Beinen behandeln wir schonend durch Sklerosierung. Dabei wird ein Verödungsmittel in die kleinen Gefäße gespritzt, die sich anschließend verschließen und verblassen. Die Behandlung erfolgt ambulant und ohne Narkose.</p>
    </div>
    <div class="service">
      <h3 class="service__title">Schaufensterkrankheit</h3>
      <p>Falls Sie nach einer bestimmten Gehstrecke pausieren müssen, weil Ihnen dann die Beine oder die Gesäßmuskulatur regelhaft schmerzen, könnten Sie unter einer Durchblutungsstörung der Beine leiden.</p>
      <p>Für die Diagnostik führen wir nach einer eingehenden Befragung eine verlässliche und unkomplizierte Ultraschalluntersuchung durch und leiten ggf. weitere Schritte ein.</p>
    </div>
    <div class="service">
      <h3 class="service__title">Pigmentflecken/kleine Hauttumore</h3>
      <p>Nach einer gründlichen Untersuchung bieten wir die chirurgische Entfernung von Pigmentflecken oder kleinen Hauttumoren an. Im Bedarfsfall werden die Befunde auch für eine mikroskopische Untersuchung weitergeschickt.</p>
    </div>
  </article>

  <article class="panel">
    <div class="photo cells-photo" role="img" aria-label="Rote Blutkörperchen in Nahaufnahme"></div>
    <div class="badge badge--cells">JETZT<br>TERMIN<em>vereinbaren</em></div>
    <div class="service">
      <h3 class="service__title">Bauchaortenaneurysma</h3>
      <p>Bei einer auch unbemerkten Erweiterung der Bauchschlagader („Aorta“), wächst mit dem Durchmesser die Gefahr einer Ruptur (Platzen) des Gefäßes.</p>
      <p>Seit Anfang 2018 haben gesetzlich krankenversicherte Männer ab 65 Jahren Anspruch auf eine einmalige Ultraschalluntersuchung zur Früherkennung von Aneurysmen der Bauchschlagader.</p>
      <p>Für die Diagnostik führen wir nach einer eingehenden Befragung eine verlässliche und unkomplizierte Ultraschalluntersuchung durch und leiten ggf. weitere Schritte ein.</p>
    </div>
    <div class="service">
      <h3 class="service__title">Bewertung des Schlaganfallrisikos</h3>
      <p>Sollten Sie unbemerkt unter Ablagerungen der Halsschlagader leiden, erhöht sich mit der zunehmenden Verengung des Gefäßes die Gefahr eines Schlaganfalles.</p>
      <p>Auch nach einer bereits durchgeführten Operation an den Halsschlaggefäßen besteht die Gefahr einer erneuten Verengung.</p>
      <p>Für die Diagnostik führen wir nach einer eingehenden Befragung eine verlässliche und unkomplizierte Ultraschalluntersuchung durch und leiten ggf. weitere Schritte ein.</p>
    </div>
  </article>

  <article class="panel">
    <div class="appointment">
      <p>Wir bieten unseren Patienten eine Terminsprechstunde an. Dies hat den Vorteil, dass Wartezeiten auf ein Minimum beschränkt werden.</p>
      <div class="hotline">
        <svg width="36" height="36" viewBox="0 0 36 36"><circle cx="18" cy="18" r="18" fill="#d1232d"/><path d="M12 10c1-1 2-1 3 0l2 3c.5 1 0 2-1 2.5 1 2 2.5 3.5 4.5 4.5.5-1 1.5-1.5 2.5-1l3 2c1 1 1 2 0 3-2 2-5 2-9-2s-6-8-5-12z" fill="#fff"/></svg>
        <div><small>Gerne vergeben wir Ihnen unter</small><span class="hotline__num">04531 5813240</span><small>einen für Sie passenden Termin.</small></div>
      </div>
    </div>
    <div class="service">
      <h3 class="service__title">Steißbeinfistel</h3>
      <p>Eine Entzündung in der Gesäßfalte kann wiederkehrende Schmerzen und Schwellungen verursachen. Wir beraten Sie ausführlich und führen den Eingriff in unserem praxiseigenen OP durch.</p>
      <p>Nach der Operation begleiten wir die Wundheilung bis zum vollständigen Abschluss und stehen Ihnen für Rückfragen jederzeit zur Verfügung.</p>
    </div>
    <div class="service">
      <h3 class="service__title">Nagelbettentzündung</h3>
      <p>Nach ausführlicher Diagnostik erfolgt eine konservative (nicht chirurgische) oder eine chirurgische Therapie. Nur bei sehr kleinen Befunden ohne Anhaltspunkte für Abszedierung und ohne Allgemeinsymptome ist eine konservative Therapie erfolgsversprechend.</p>
    </div>
    <div class="service">
      <h3 class="service__title">Durchblutungsstörung Hand/Fuß</h3>
      <p>Sollten Sie regelhaft insbesondere z.B. nach Kältereiz unter einer blau – weiß – roten Verfärbung der Hände leiden, könnten Sie unter dem sogenannten „Raynaud-Syndrom“ leiden.</p>
      <p>Für die Diagnostik führen wir nach einer eingehenden Befragung eine verlässliche und unkomplizierte Ultraschalluntersuchung durch und leiten gegebenenfalls weitere Schritte ein.</p>
    </div>
  </article>
</section>

</body>
</html>
```